One of Australia's fastest growing Financial Company looking for an updated business card design!

Meridale Holdings Australia is looking for an updated design for our business cards. We would like to keep up our professional appearances and have get new exciting design that fits our company.

The Meridale aim is to facilitate and assist clients in every financial requirement that may arise in financial areas.

We would to see the design to use colour blue and we like the clouds in the background. We have attached two designs we have use before but we need something with more professional and easy to read design.

We would like the website in the back of the card; the employees name more central and stands out; only a postal address; a list of all our locations along the bottom (Sydney, Melbourne, Brisbane, Singapore)

Looking forward to seeing the designs come in!

Target Market(s)

Other Industry Professionals
Middle Class Families

Industry/Entity Type

Finance

Contact Information for Business Card

Name; Company Role; Office Number; Mobile Number; Email Address; Website; Postal Address; Locations

Font styles to use
Serif
Sans Serif

Colors
0492cd
33a6d7
85cae6
85acd3
3176b5
0455a3
cee9f5
d5e2ee

Requirements
Must have
• Name; Company Role; Office Number; Mobile Number; Email Address; Website; Postal Address; Locations
Nice to have
• The colour blue, clouds on the background

```html
<!DOCTYPE html>
<html lang="en">
<head>
<meta charset="utf-8">
<title>Meridale Holdings Australia – Business Card</title>
<link rel="stylesheet" href="https://fonts.googleapis.com/css2?family=Montserrat:wght@300;400;600&display=swap">
<style>
  :root {
    --page-bg: #1c1c1f;
    --card-left: #2e3a68;
    --card-right: #22408f;
    --rule: #33a6d7;
    --accent: #33a6d7;
    --logo-bg: #e9ecf1;
    --logo-ink: #0455a3;
    --text-light: #ffffff;
    --text-muted: #a8b4cc;
  }
  * { box-sizing: border-box; margin: 0; padding: 0; }
  html, body {
    width: 1200px; height: 797px; overflow: hidden;
    background: var(--page-bg);
    font-family: "Montserrat", sans-serif;
  }
  .card {
    position: absolute; left: 160px; top: 130px;
    width: 880px; height: 537px;
    background: linear-gradient(100deg, var(--card-left) 0%, var(--card-right) 100%);
    border-radius: 4px;
    box-shadow: 0 14px 30px rgba(0,0,0,0.5);
    overflow: hidden;
  }
  .brand { position: absolute; left: 34px; top: 34px; }
  .brand-plate {
    display: flex; align-items: center; gap: 12px;
    width: 300px; height: 70px; padding: 0 18px;
    background: var(--logo-bg);
  }
  .brand-square { width: 22px; height: 22px; background: var(--logo-ink); }
  .brand-name { font-size: 38px; font-weight: 600; color: var(--logo-ink); }
  .brand-tagline { margin-top: 6px; font-size: 15px; font-weight: 600; color: var(--accent); }

  .divider { position: absolute; left: 0; top: 0; }

  .person { position: absolute; left: 470px; top: 216px; width: 230px; }
  .person-name { font-size: 32px; font-weight: 600; color: var(--text-light); letter-spacing: 0.5px; line-height: 40px; }
  .person-role { margin-top: 14px; margin-left: 18px; font-size: 19px; font-weight: 400; color: var(--accent); line-height: 24px; }

  .contacts {
    position: absolute; right: 30px; top: 282px;
    list-style: none;
    display: flex; flex-direction: column; align-items: flex-end; gap: 4px;
  }
  .contact { display: flex; align-items: center; gap: 8px; color: var(--text-light); font-weight: 300; }
  .contact svg { flex: none; }
  .contact-label { font-weight: 600; color: var(--accent); font-size: 15px; }
  .contact-phone { font-size: 22px; line-height: 30px; }
  .contact-email { font-size: 24px; line-height: 34px; }
  .contact-web { font-size: 26px; line-height: 36px; margin-top: 6px; }

  .address {
    position: absolute; left: 20px; bottom: 18px;
    font-style: normal;
    font-size: 15px; font-weight: 300; line-height: 1.35; color: var(--text-muted);
  }
  .locations {
    position: absolute; right: 30px; bottom: 22px;
    list-style: none; display: flex; gap: 10px;
    font-size: 15px; font-weight: 400; color: var(--text-muted); letter-spacing: 0.5px;
  }
  .locations li + li::before { content: "·"; color: var(--accent); margin-right: 10px; }
</style>
</head>
<body>
  <main class="card">
    <div class="brand">
      <div class="brand-plate">
        <span class="brand-square"></span>
        <span class="brand-name">Meridale</span>
      </div>
      <p class="brand-tagline">Investments Holdings Australia</p>
    </div>

    <svg class="divider" width="880" height="537" viewBox="0 0 880 537" aria-hidden="true">
      <line x1="0" y1="266" x2="455" y2="266" stroke="var(--rule)" stroke-width="1.2"/>
      <line x1="700" y1="266" x2="880" y2="266" stroke="var(--rule)" stroke-width="1.2"/>
    </svg>

    <div class="person">
      <h1 class="person-name">Daniel Hart</h1>
      <p class="person-role">Manager</p>
    </div>

    <ul class="contacts">
      <li class="contact contact-phone">
        <span class="contact-label">Office</span>
        <svg width="18" height="18" viewBox="0 0 24 24" fill="none" stroke="var(--accent)" stroke-width="2"><path d="M5 3h4l2 5-2.5 1.5a11 11 0 0 0 6 6L16 13l5 2v4a2 2 0 0 1-2 2A16 16 0 0 1 3 5a2 2 0 0 1 2-2z"/></svg>
        02 5550 1840
      </li>
      <li class="contact contact-phone">
        <span class="contact-label">Mobile</span>
        <svg width="18" height="18" viewBox="0 0 24 24" fill="none" stroke="var(--accent)" stroke-width="2"><path d="M5 3h4l2 5-2.5 1.5a11 11 0 0 0 6 6L16 13l5 2v4a2 2 0 0 1-2 2A16 16 0 0 1 3 5a2 2 0 0 1 2-2z"/></svg>
        041 555 208 73
      </li>
      <li class="contact contact-email">
        <svg width="20" height="16" viewBox="0 0 24 18" fill="none" stroke="var(--accent)" stroke-width="2"><rect x="1" y="1" width="22" height="16"/><path d="M1 1l11 9 11-9"/></svg>
        daniel.hart@meridale.com.au
      </li>
      <li class="contact contact-web">
        <svg width="20" height="20" viewBox="0 0 24 24" fill="none" stroke="var(--accent)" stroke-width="2.2"><path d="M10 14a4 4 0 0 0 6 0l4-4a4 4 0 0 0-6-6l-1 1"/><path d="M14 10a4 4 0 0 0-6 0l-4 4a4 4 0 0 0 6 6l1-1"/></svg>
        meridaleholdingsaustralia.com.au
      </li>
    </ul>

    <address class="address">
      PO Box 418<br>
      Norwood NSW 2160
    </address>

    <ul class="locations">
      <li>Sydney</li>
      <li>Melbourne</li>
      <li>Brisbane</li>
      <li>Singapore</li>
    </ul>
  </main>
</body>
</html>
```